brivox new business card design project

we need a new business card design. you can view info about us @ brivox.com. i have attached an example of our previous card with our previous name that we no longer use. We really liked the design, colors etc. look below to see more info about this project. it asks for a limited number of words. please see our website for more info about our compnay.

Target Market(s)

law enforcement

Contact Information for Business Card

i have uploaded an example of what we used before that we liked.

Font styles to use
Serif

```html
<!DOCTYPE html>
<html lang="en">
<head>
<meta charset="utf-8">
<title>Brivox Business Card</title>
<link rel="stylesheet" href="https://fonts.googleapis.com/css2?family=Exo+2:wght@500&family=Roboto:wght@300;400&display=swap">
<style>
  :root {
    --backdrop: #a8a8a8;
    --navy: #04121c;
    --navy-glow: #0b2a38;
    --brand-blue: #1466a8;
    --paper: #f3f3f3;
    --ink: #1e2328;
    --white: #ffffff;
    --silver: #e2e2e2;
  }
  * { margin: 0; padding: 0; box-sizing: border-box; }
  html, body {
    width: 1200px; height: 576px; overflow: hidden;
    background: var(--backdrop);
    font-family: "Roboto", Arial, sans-serif;
  }
  .canvas { position: relative; width: 1200px; height: 576px; }
  .card {
    position: absolute; border-radius: 11px; overflow: hidden;
    box-shadow: 2px 4px 8px rgba(0,0,0,0.25);
  }
  /* Front */
  .card-front { left: 82px; top: 139px; width: 484px; height: 292px; background: var(--navy); }
  .network-map {
    position: absolute; left: 28px; top: 28px; width: 430px; height: 240px;
    background: radial-gradient(ellipse at 50% 45%, var(--navy-glow) 0%, rgba(11,42,56,0.35) 45%, rgba(4,18,28,0) 75%);
  }
  .front-logo {
    position: absolute; left: 0; right: 0; top: 98px; text-align: center;
    font-weight: 300; font-size: 52px; letter-spacing: 5px; color: var(--white);
  }
  .front-stripes { position: absolute; left: 0; bottom: 0; width: 290px; height: 23px; }
  .front-url {
    position: absolute; right: 26px; bottom: 9px;
    font-size: 13px; font-weight: 300; letter-spacing: 3px; color: var(--silver);
  }
  /* Back */
  .card-back { left: 602px; top: 138px; width: 480px; height: 291px; background: var(--paper); }
  .side-band { position: absolute; left: 0; top: 0; bottom: 0; width: 34px; background: var(--navy); }
  .side-rule { position: absolute; left: 36px; top: 0; bottom: 0; width: 3px; background: var(--brand-blue); }
  .back-logo {
    position: absolute; left: 60px; top: 56px;
    font-weight: 300; font-size: 48px; letter-spacing: 4px; color: var(--ink);
  }
  .person-name {
    position: absolute; left: 59px; top: 136px;
    font-family: "Exo 2", Arial, sans-serif; font-weight: 500; font-size: 20px; color: var(--brand-blue);
  }
  .person-title { position: absolute; left: 59px; top: 164px; font-size: 11.5px; color: var(--ink); }
  .contact-list { position: absolute; left: 59px; top: 193px; list-style: none; }
  .contact-list li {
    display: flex; align-items: center; height: 18px;
    font-size: 13px; font-weight: 300; color: var(--ink);
  }
  .contact-list svg { width: 12px; height: 12px; margin-right: 13px; fill: var(--navy); }
  .address { position: absolute; left: 59px; top: 253px; font-size: 13px; color: var(--ink); }
</style>
</head>
<body>
<div class="canvas">
  <section class="card card-front">
    <div class="network-map" role="img" aria-label="Faint network map of the country with connected dots"></div>
    <div class="front-logo">BRIVOX</div>
    <svg class="front-stripes" viewBox="0 0 290 23" aria-hidden="true">
      <polygon points="0,0 194,0 180,23 0,23" fill="var(--brand-blue)"/>
      <polygon points="210,0 271,0 257,23 196,23" fill="var(--silver)"/>
    </svg>
    <div class="front-url">www.brivox.com</div>
  </section>

  <section class="card card-back">
    <div class="side-band"></div>
    <div class="side-rule"></div>
    <div class="back-logo">BRIVOX</div>
    <h1 class="person-name">Daniel Marsh</h1>
    <p class="person-title">Founder/Chief Executive Officer</p>
    <ul class="contact-list">
      <li>
        <svg viewBox="0 0 12 12" aria-hidden="true"><path d="M1 4c0-2 2-3 5-3s5 1 5 3v1H8V4H4v1H1zM3 6h6l2 5H1z"/></svg>
        800.555.0142
      </li>
      <li>
        <svg viewBox="0 0 12 12" aria-hidden="true"><path d="M0 2h12v8H0z M1 3l5 4 5-4" stroke="#f3f3f3" stroke-width="0.9"/></svg>
        info@brivox.com
      </li>
      <li>
        <svg viewBox="0 0 12 12" aria-hidden="true"><circle cx="6" cy="6" r="5.5"/><path d="M0.5 6h11M6 0.5v11M6 0.5c-3 3-3 8 0 11M6 0.5c3 3 3 8 0 11" stroke="#f3f3f3" stroke-width="0.7" fill="none"/></svg>
        www.brivox.com
      </li>
    </ul>
    <p class="address">4120 Lakeline Avenue Austin, TX 78731</p>
  </section>
</div>
</body>
</html>
```